Create a Capability Summary in PowerPoint

CAPABILITY SUMMARY:
We have been asked to provide a Capability Summary by a client and we need your help creating a compelling document!
Our firm specializes in placing cleared technical talent with innovative government contracting firms nationwide. Our goal is to position ourselves as the "go to" talent acquisition company for small and large IT contracting firms in the Federal IT market.
We want you to have creative control over this template, but would like to it include some variation of the following:
Cover Slide w/ Logo
About Us
The Vantrel Difference
Benefits We Offer
-noting that, unlike many recruiting forms, we offer generous PTO, 100%
vesting 401K, and healthcare benefits for all employees
The Talent We Work With
-showcase the fact that we work in the following technical areas:
Network & Systems Engineer, Software Development, Data Science,
and Information Assurance
Clients We Work With
Data-Driven Recruiting Process
-funnel or graphic showcasing our multi-stage recruiting process of :
Sourcing -> Data Discovery -> Automated Outreach -> Candidate
Qualification -> Technical Interview -> Offer & On-boarding
Contact Us
Target Market(s)
IT companies looking for top engineering talent.

```html
<!DOCTYPE html>
<html lang="en">
<head>
<meta charset="utf-8">
<title>Vantrel – Capability Summary Template</title>
<link href="https://fonts.googleapis.com/css2?family=Montserrat:wght@400;600;800&family=Open+Sans:ital,wght@0,400;0,600;0,700;1,400&display=swap" rel="stylesheet">
<style>
:root{
  --navy:#1b3a6b;
  --blue:#1f6fb2;
  --cyan:#1aa3d9;
  --red:#d9432b;
  --ink:#1d1d1d;
  --grey:#6b6f76;
  --paper:#ffffff;
  --mist:#eef0f3;
  --shadow:0 3px 10px rgba(0,0,0,.18);
}
*{box-sizing:border-box;margin:0;padding:0}
html,body{width:1200px;height:2200px;overflow:hidden;background:var(--paper)}
body{position:relative;font-family:"Open Sans",Arial,sans-serif;color:var(--ink)}

.slide{position:absolute;width:560px;height:315px;background:var(--paper);box-shadow:var(--shadow);overflow:hidden}
.col-left{left:32px}.col-right{left:616px}
.row-1{top:468px}.row-2{top:810px}.row-3{top:1152px}.row-4{top:1494px}.row-5{top:1836px}

.slide-logo{position:absolute;left:16px;top:12px;font-family:"Montserrat",sans-serif;font-weight:800;font-size:15px;letter-spacing:1px;color:var(--navy)}
.slide-next{position:absolute;right:14px;top:12px;width:12px;height:18px}
.photo{position:absolute}
.title{font-family:"Montserrat",sans-serif;font-weight:800;color:var(--navy);line-height:1.1}
.body-text{font-size:9px;line-height:1.5;color:var(--grey)}

/* cover */
.cover{position:absolute;left:32px;top:24px;width:720px;height:405px;box-shadow:var(--shadow);overflow:hidden;
  background:linear-gradient(180deg,#5c6f8c 0%,#8d8fa3 40%,#c7a59a 70%,#9a8b86 100%)}
.cover-band{position:absolute;left:0;top:118px;width:100%;height:150px;background:rgba(255,255,255,.82)}
.cover-name{position:absolute;left:0;width:100%;top:150px;text-align:center;font-family:"Montserrat",sans-serif;font-weight:800;font-size:72px;letter-spacing:4px;color:var(--blue)}
.cover-sub{position:absolute;left:0;width:100%;top:236px;text-align:center;font-family:"Montserrat",sans-serif;font-weight:600;font-size:13px;letter-spacing:3px;color:var(--navy)}

/* feature list */
.features{position:absolute;left:790px;top:30px;font-family:"Open Sans",Arial,sans-serif;font-weight:700;font-size:21px;line-height:1.5;color:var(--ink);list-style:none}
.features li{display:flex;align-items:center;gap:12px}
.features .box{width:16px;height:16px;border:2px solid var(--ink)}
.features .sub{padding-left:60px;gap:16px;font-size:20px}
.features .dot{width:8px;height:8px;border-radius:50%;background:var(--ink)}

/* about */
.about-panel{position:absolute;right:0;top:0;width:330px;height:315px;background:rgba(255,255,255,.94);clip-path:polygon(22% 0,100% 0,100% 100%,0 100%)}
.about .title{position:absolute;left:260px;top:120px;font-size:24px;color:var(--navy)}
.about .body-text{position:absolute;left:300px;top:160px;width:230px}

/* difference */
.diff-panel{position:absolute;right:0;top:0;width:260px;height:315px;background:var(--paper);clip-path:polygon(30% 0,100% 0,100% 100%,0 100%)}
.diff .lead{position:absolute;left:380px;top:70px;font-family:"Montserrat",sans-serif;font-weight:600;font-size:13px;color:var(--red)}
.diff .title{position:absolute;left:360px;top:88px;font-size:24px;color:var(--red)}
.diff .body-text{position:absolute;left:380px;top:130px;width:160px}

/* benefits */
.benefits .title{position:absolute;left:300px;top:70px;font-size:22px}
.benefit-list{position:absolute;left:300px;top:140px;list-style:none}
.benefit-list li{margin-bottom:10px;font-size:10px;font-weight:700;color:var(--navy)}
.benefit-list span{display:block;font-weight:400;font-size:8px;color:var(--grey)}

/* quote */
.quote blockquote{position:absolute;left:270px;top:78px;width:260px;font-style:italic;font-size:17px;line-height:1.45;color:var(--navy)}
.quote cite{position:absolute;right:40px;top:238px;font-size:11px;font-style:italic;color:var(--grey)}

/* valued clients */
.client-grid{position:absolute;left:40px;top:70px;display:grid;grid-template-columns:repeat(2,100px);gap:18px 28px}
.client-mark{display:flex;align-items:center;gap:6px;font-family:"Open Sans",sans-serif;font-weight:700;font-size:10px;color:var(--grey)}
.client-mark i{display:block;width:12px;height:12px;background:var(--blue)}
.valued .title{position:absolute;left:310px;top:90px;font-size:22px;font-weight:600}
.valued .body-text{position:absolute;left:310px;top:155px;width:210px}
.divider{position:absolute;left:290px;top:70px;width:1px;height:200px;background:#d5d8dd}

/* clients work */
.work .title{position:absolute;left:345px;top:72px;font-size:22px}
.work ul{position:absolute;left:345px;top:150px;list-style:none;font-size:10px;line-height:2;color:var(--grey)}

/* talent */
.talent .center{position:absolute;left:150px;top:0;width:260px;height:315px}
.talent .role{position:absolute;font-family:"Montserrat",sans-serif;font-weight:600;font-size:12px;color:var(--navy);line-height:1.3}
.talent .title{position:absolute;left:0;width:100%;top:140px;text-align:center;font-size:18px}
.talent .rule{position:absolute;left:20px;right:20px;height:1px;background:var(--navy)}

/* process */
.process .title{position:absolute;left:22px;top:110px;font-size:20px}
.process .funnel{position:absolute;left:200px;top:46px;width:170px;height:210px}
.process ol{position:absolute;left:385px;top:56px;list-style:none;font-size:10px;font-weight:600;line-height:33px;color:var(--navy)}

/* contact */
.contact-box{position:absolute;left:250px;top:60px;width:270px;height:210px;background:var(--cyan);color:#fff;padding:70px 24px 0 28px}
.contact-box .title{position:absolute;left:28px;top:22px;color:#fff;font-size:22px}
.contact-box p{font-size:10px;line-height:1.7}

/* thanks */
.thanks-name{position:absolute;left:0;width:100%;top:100px;text-align:center;font-family:"Montserrat",sans-serif;font-weight:800;font-size:44px;letter-spacing:3px;color:var(--navy)}
.thanks-sub{position:absolute;left:0;width:100%;top:160px;text-align:center;font-family:"Montserrat",sans-serif;font-weight:600;font-size:13px;letter-spacing:3px;color:var(--blue)}
</style>
</head>
<body>

<section class="cover">
  <div class="photo" role="img" aria-label="Person standing on a hill under a soft dusk sky" style="inset:0;background:linear-gradient(180deg,#4e6382 0%,#8a8ea6 45%,#caa69a 72%,#6f6462 100%)"></div>
  <div class="cover-band"></div>
  <div class="cover-name">VANTREL</div>
  <div class="cover-sub">BUSINESS PRESENTATION TEMPLATE</div>
</section>

<ul class="features">
  <li><span class="box"></span>Ratio 16:9</li>
  <li><span class="box"></span>Full HD</li>
  <li><span class="box"></span>Master Slides &nbsp;easy change</li>
  <li><span class="box"></span>Up to 50 slides</li>
  <li class="sub"><span class="dot"></span>Text Slides</li>
  <li class="sub"><span class="dot"></span>Text +Images</li>
  <li class="sub"><span class="dot"></span>Data Slides</li>
  <li class="sub"><span class="dot"></span>Tables</li>
  <li class="sub"><span class="dot"></span>Infographics</li>
</ul>

<!-- About us -->
<section class="slide about col-left row-1">
  <div class="photo" role="img" aria-label="Team working at an office desk" style="inset:0;background:linear-gradient(120deg,#2f3440 0%,#5b5f6a 50%,#8a8d94 100%)"></div>
  <div class="about-panel"></div>
  <div class="slide-logo" style="color:#fff">VANTREL</div>
  <svg class="slide-next" viewBox="0 0 12 18"><path d="M2 2l7 7-7 7" fill="none" stroke="var(--red)" stroke-width="3"/></svg>
  <h2 class="title">ABOUT US</h2>
  <p class="body-text">We place cleared technical talent with government contractors nationwide, matching proven engineers to mission work.</p>
</section>

<!-- Difference -->
<section class="slide diff col-right row-1">
  <div class="photo" role="img" aria-label="Hands typing on a laptop at a desk" style="inset:0;background:linear-gradient(135deg,#c9c3bd 0%,#9b948e 45%,#5a5552 100%)"></div>
  <div class="diff-panel"></div>
  <svg class="slide-next" viewBox="0 0 12 18"><path d="M2 2l7 7-7 7" fill="none" stroke="var(--red)" stroke-width="3"/></svg>
  <div class="lead">The <span style="color:var(--navy)">Vantrel</span></div>
  <h2 class="title">DIFFERENCE</h2>
  <p class="body-text">Our recruiters know cleared IT work, so every candidate we send is vetted, ready and fit for the role.</p>
</section>

<!-- Benefits -->
<section class="slide benefits col-left row-2">
  <div class="slide-logo">VANTREL</div>
  <svg class="slide-next" viewBox="0 0 12 18"><path d="M2 2l7 7-7 7" fill="none" stroke="var(--red)" stroke-width="3"/></svg>
  <div class="photo" role="img" aria-label="Colleagues shaking hands" style="left:20px;top:60px;width:120px;height:220px;background:linear-gradient(180deg,#b8bcc2,#6e737b)"></div>
  <div class="photo" role="img" aria-label="Team meeting around a table" style="left:148px;top:60px;width:120px;height:220px;background:linear-gradient(180deg,#d4cdc4,#8d8378)"></div>
  <h2 class="title">BENEFITS<br>WE OFFER</h2>
  <ul class="benefit-list">
    <li>Generous PTO<span>Paid time off for all staff</span></li>
    <li>100% Vesting 401K<span>Fully vested from day one</span></li>
    <li>Healthcare Benefits<span>Medical, dental and vision</span></li>
  </ul>
</section>

<!-- Quote -->
<section class="slide quote col-right row-2">
  <div class="slide-logo">VANTREL</div>
  <svg class="slide-next" viewBox="0 0 12 18"><path d="M2 2l7 7-7 7" fill="none" stroke="var(--red)" stroke-width="3"/></svg>
  <div class="photo" role="img" aria-label="Portrait of a smiling executive in a suit" style="left:30px;top:60px;width:200px;height:230px;background:linear-gradient(180deg,#e1e3e6 0%,#a9adb3 55%,#3a4150 100%)"></div>
  <blockquote>"I believe in Vantrel because is a company delivering exactly what the customer needs to get the best job done."</blockquote>
  <cite>— Alan Mercer</cite>
</section>

<!-- Valued clients -->
<section class="slide valued col-left row-3">
  <div class="slide-logo">VANTREL</div>
  <svg class="slide-next" viewBox="0 0 12 18"><path d="M2 2l7 7-7 7" fill="none" stroke="var(--red)" stroke-width="3"/></svg>
  <div class="client-grid">
    <div class="client-mark"><i></i>Corvane</div>
    <div class="client-mark"><i style="background:var(--red)"></i>Helix Nine</div>
    <div class="client-mark"><i style="background:#3aa55b"></i>Stratum</div>
    <div class="client-mark"><i style="background:var(--navy)"></i>Nortide</div>
    <div class="client-mark"><i style="background:#8a8d94"></i>Byrelle</div>
    <div class="client-mark"><i style="background:var(--cyan)"></i>Quadra</div>
  </div>
  <div class="divider"></div>
  <h2 class="title">Our Valued<br>Clients</h2>
  <p class="body-text">Small and large IT firms in the federal market trust us to staff their key programs.</p>
</section>

<!-- Clients we work with -->
<section class="slide work col-right row-3">
  <div class="slide-logo">VANTREL</div>
  <svg class="slide-next" viewBox="0 0 12 18"><path d="M2 2l7 7-7 7" fill="none" stroke="var(--red)" stroke-width="3"/></svg>
  <div class="photo" role="img" aria-label="Blue glowing server racks" style="left:20px;top:50px;width:300px;height:250px;background:linear-gradient(160deg,#0f2a5a 0%,#1f5fa8 55%,#4aa3e0 100%);clip-path:polygon(12% 0,34% 0,22% 100%,0 100%,0 100%,12% 0,38% 0,60% 0,48% 100%,26% 100%,38% 0,64% 0,88% 0,76% 100%,52% 100%,64% 0)"></div>
  <h2 class="title">CLIENTS WE<br>WORK WITH</h2>
  <ul>
    <li>Federal IT Primes</li>
    <li>Cyber Contractors</li>
    <li>Cloud Integrators</li>
    <li>Defense Software Firms</li>
  </ul>
</section>

<!-- Talent -->
<section class="slide talent col-left row-4">
  <div class="photo" role="img" aria-label="Engineer at a computer workstation" style="left:0;top:0;width:150px;height:315px;background:linear-gradient(180deg,#4a4f58,#1f232a)"></div>
  <div class="photo" role="img" aria-label="Network cables in a server room" style="left:410px;top:0;width:150px;height:315px;background:linear-gradient(180deg,#6d7380,#2b303a)"></div>
  <div class="center">
    <div class="role" style="left:20px;top:60px">Network &amp;<br>Systems<br>Engineer</div>
    <div class="role" style="right:20px;top:60px;text-align:right">Data<br>Science</div>
    <div class="rule" style="top:128px"></div>
    <h2 class="title">THE TALENT WE<br>WORK WITH</h2>
    <div class="rule" style="top:192px"></div>
    <div class="role" style="left:20px;top:210px">Software<br>Development</div>
    <div class="role" style="right:20px;top:210px;text-align:right">Information<br>Assurance</div>
  </div>
</section>

<!-- Recruiting process -->
<section class="slide process col-right row-4">
  <div class="slide-logo">VANTREL</div>
  <svg class="slide-next" viewBox="0 0 12 18"><path d="M2 2l7 7-7 7" fill="none" stroke="var(--red)" stroke-width="3"/></svg>
  <h2 class="title">RECRUITING<br>PROCESS</h2>
  <svg class="funnel" viewBox="0 0 170 210">
    <polygon points="0,0 170,0 156,33 14,33" fill="#d9432b"/>
    <polygon points="15,35 155,35 141,68 29,68" fill="#ec7a2c"/>
    <polygon points="30,70 140,70 126,103 44,103" fill="#f2b534"/>
    <polygon points="45,105 125,105 111,138 59,138" fill="#2aa3a1"/>
    <polygon points="60,140 110,140 98,173 72,173" fill="#1f6fb2"/>
    <polygon points="73,175 97,175 85,210" fill="#1b3a6b"/>
  </svg>
  <ol>
    <li>Sourcing</li>
    <li>Data Discovery</li>
    <li>Automated Outreach</li>
    <li>Candidate Qualification</li>
    <li>Technical Interview</li>
    <li>Offer &amp; On-boarding</li>
  </ol>
</section>

<!-- Contact -->
<section class="slide contact col-left row-5">
  <div class="photo" role="img" aria-label="Street map of the office location" style="inset:0;background:linear-gradient(135deg,#eef0ea 0%,#dfe4dc 50%,#cfd8d6 100%)"></div>
  <div class="contact-box">
    <h2 class="title">GET IN TOUCH</h2>
    <p>Vantrel Talent Group<br>1200 Harbor Point Ave, Suite 400<br>Arlington, VA 22201<br>+1 555 013 2040<br>hello@vantrel.com</p>
  </div>
</section>

<!-- Thanks -->
<section class="slide thanks col-right row-5">
  <div class="photo" role="img" aria-label="Figure on a beach at sunset" style="inset:0;background:linear-gradient(180deg,#eef1f5 0%,#d8dde5 45%,#c6b39c 75%,#8c7a66 100%)"></div>
  <div class="thanks-name">VANTREL</div>
  <div class="thanks-sub">THANKS FOR WATCHING</div>
</section>

</body>
</html>
```